Business card for Internet Marketing Consultant

Simple - need a nice business card design using the logo elements and colors. Keywords: Progressive, professional, stylish, minimalist. Please use the bc as part of the design.

Info for card:

Gareth Pennick
Internet Marketing Strategist
Phone: (520) 318-6047
Email: gareth@brightcanopy.com
Address: 2915 W. Larkmoor Ave., Ste. 118
Tucson, Arizona 85293

Website: www.brightcanopy.com

Industry/Entity Type

Business

Font styles to use
Sans Serif

```html
<!DOCTYPE html>
<html lang="en">
<head>
<meta charset="utf-8">
<title>brightcanopy business card</title>
<link href="https://fonts.googleapis.com/css2?family=Open+Sans:wght@400;600&display=swap" rel="stylesheet">
<style>
  :root {
    --blue: #2f6db5;
    --green: #5cb86a;
    --ink: #1b1b1b;
    --muted: #6f7377;
    --card: #fbfbf9;
    --backdrop: #f1f1f1;
  }
  * { margin: 0; padding: 0; box-sizing: border-box; }
  html, body {
    width: 1200px;
    height: 418px;
    overflow: hidden;
    background: var(--backdrop);
    font-family: "Open Sans", Arial, sans-serif;
  }
  .canvas { position: relative; width: 1200px; height: 418px; }
  .card {
    position: absolute;
    top: 38px;
    width: 512px;
    height: 344px;
    background: var(--card);
    border: 1px solid #e2e2de;
  }
  .card--front { left: 72px; }
  .card--back { left: 637px; }

  .wordmark {
    color: var(--blue);
    font-weight: 600;
    letter-spacing: -0.5px;
    white-space: nowrap;
  }
  .tagline {
    color: var(--muted);
    text-transform: uppercase;
    letter-spacing: 2.2px;
    white-space: nowrap;
  }

  .front-brand { position: absolute; left: 220px; top: 30px; }
  .front-brand .wordmark { font-size: 30px; line-height: 36px; }
  .front-brand .tagline { font-size: 10.5px; margin-top: 2px; }

  .holder-name {
    position: absolute;
    left: 215px;
    top: 114px;
    font-size: 28px;
    font-weight: 400;
    color: var(--ink);
    white-space: nowrap;
  }
  .contact-list {
    position: absolute;
    left: 215px;
    top: 184px;
    list-style: none;
    font-size: 17px;
    line-height: 23px;
    color: var(--ink);
    white-space: nowrap;
  }
  .contact-list .label { color: var(--blue); margin-right: 5px; }
  .contact-list .continued { padding-left: 6px; }

  .back-brand {
    position: absolute;
    left: 0; right: 0;
    top: 70px;
    text-align: center;
  }
  .back-brand .mark { display: block; margin: 0 auto 14px; }
  .back-brand .wordmark { font-size: 46px; line-height: 54px; }
  .back-brand .tagline { font-size: 13px; letter-spacing: 3px; margin-top: 4px; }
</style>
</head>
<body>
<main class="canvas">
  <section class="card card--front" aria-label="Business card front">
    <div class="front-brand">
      <div class="wordmark">brightcanopy</div>
      <div class="tagline">Internet Marketing Strategies</div>
    </div>
    <h1 class="holder-name">Gareth Pennick</h1>
    <ul class="contact-list">
      <li><span class="label">P:</span>(520) 318-6047</li>
      <li><span class="label">E:</span>gareth@brightcanopy.com</li>
      <li><span class="label">W:</span>www.brightcanopy.com</li>
      <li><span class="label">A:</span>2915 W. Larkmoor Ave.,</li>
      <li class="continued">Ste. 118 | Tucson, Arizona 85293</li>
    </ul>
  </section>

  <section class="card card--back" aria-label="Business card back">
    <div class="back-brand">
      <svg class="mark" width="56" height="56" viewBox="0 0 56 56" aria-hidden="true">
        <circle cx="28" cy="28" r="26" fill="var(--green)"/>
      </svg>
      <div class="wordmark">brightcanopy</div>
      <div class="tagline">Internet Marketing Strategies</div>
    </div>
  </section>
</main>
</body>
</html>
```